Calendar Ad / Flyer

Our law firm needs a calendar ad to place in a local calendar.
THE DEADLINE IS THIS THURSDAY 06/28/2018.

Attached is the ad used in last years calendar. A few notes on this...
**. This is by no means the model to follow.
Please be creative and do what makes more sense marketing wise.
1. Need to update the color scheme which corresponds to the new website at marvolinlegal.com
2. The "MARVOLIN LAW | SHAPING FAITH WITH RESULTS" should be put at the top and made larger
3. "KNOWN AND TRUSTED IN OUR COMMUNITY FOR OVER 21 YEARS" should be changed to "KNOWN AND TRUSTED IN OUR COMMUNITY FOR OVER 22 YEARS"
4. "Gordon R. Marvolin, Esq." should be made larger and better positioned.
5. Under the list of practices, it should be changed to have:
"Personal Injury, Legal Malpractice, Unlicensed Contractors, Medical Malpractice, Civil Litigation"
6. Contact information (i.e. contact number, website, and address) should be better positioned
7. Placement of endorsement logos should stand out more.
8. New picture of head attorney is attached.

Last but not least... Give it your best shot!

```html
<!DOCTYPE html>
<html lang="en">
<head>
<meta charset="utf-8">
<title>Marvolin Law — Calendar Ad</title>
<link rel="stylesheet" href="https://fonts.googleapis.com/css2?family=Lato:wght@400;700&family=Montserrat:wght@500;600&display=swap">
<style>
  :root {
    --charcoal: #3b3b3d;
    --slate: #5f6063;
    --gold: #c9a673;
    --mist: #efefef;
    --white: #ffffff;
    --ink: #3c3c3c;
    --text-grey: #5a5a5a;
    --tag-grey: #d6d6d6;
  }
  html, body {
    margin: 0;
    padding: 0;
    overflow: hidden;
    background: var(--white);
  }
  .ad {
    position: relative;
    width: 1200px;
    height: 899px;
    overflow: hidden;
    font-family: "Lato", Arial, sans-serif;
    background: var(--white);
  }
  .ad__shapes {
    position: absolute;
    inset: 0;
  }
  .ad__portrait {
    position: absolute;
    left: 505px;
    top: 0;
    width: 695px;
    height: 500px;
    clip-path: polygon(330px 0, 695px 0, 695px 500px, 0 500px, 8px 440px, 200px 400px, 320px 330px, 335px 180px);
    background:
      linear-gradient(180deg, rgba(110,110,113,0) 0%, rgba(110,110,113,0) 66%, #707073 78%, #646467 100%),
      radial-gradient(ellipse 170px 230px at 495px 220px, #b48f7b 0%, #a58472 55%, rgba(120,110,105,0) 100%),
      radial-gradient(ellipse 90px 80px at 495px 440px, #f2f2f2 0%, rgba(240,240,240,0) 100%),
      linear-gradient(90deg, #5d5e61 0%, #7b7b7e 50%, #8c8c8f 100%);
  }
  .brand {
    position: absolute;
    left: 92px;
    top: 168px;
    font-family: "Montserrat", Arial, sans-serif;
    font-weight: 600;
    font-size: 62px;
    letter-spacing: 3px;
    line-height: 1;
    color: var(--gold);
    white-space: nowrap;
  }
  .brand__mark {
    display: inline-block;
    width: 48px;
    height: 48px;
    margin-left: 14px;
    vertical-align: 0;
    background: var(--gold);
  }
  .tagline {
    position: absolute;
    left: 240px;
    top: 228px;
    font-family: "Montserrat", Arial, sans-serif;
    font-weight: 500;
    font-size: 22px;
    letter-spacing: 1.5px;
    color: var(--tag-grey);
    white-space: nowrap;
  }
  .claim {
    position: absolute;
    left: 84px;
    top: 381px;
    margin: 0;
    font-size: 25.5px;
    line-height: 32px;
    color: var(--ink);
  }
  .practices {
    position: absolute;
    left: 92px;
    top: 528px;
    margin: 0;
    padding: 0;
    list-style: none;
  }
  .practices__item {
    position: relative;
    padding-left: 40px;
    height: 46.8px;
    font-size: 31.5px;
    line-height: 40px;
    color: var(--text-grey);
  }
  .practices__item svg {
    position: absolute;
    left: 2px;
    top: 13px;
  }
  .attorney {
    position: absolute;
    left: 650px;
    top: 524px;
    width: 555px;
    text-align: center;
    font-weight: 700;
    font-size: 34px;
    color: var(--white);
    white-space: nowrap;
  }
  .contact {
    position: absolute;
    top: 806px;
    font-size: 38px;
    font-weight: 700;
    color: var(--text-grey);
    white-space: nowrap;
    line-height: 48px;
  }
  .contact svg {
    vertical-align: -4px;
    margin-right: 8px;
  }
  .contact--phone { left: 84px; }
  .contact--web { left: 444px; }
  .address {
    position: absolute;
    left: 860px;
    top: 799px;
    width: 310px;
    text-align: center;
    font-weight: 700;
    font-size: 18px;
    line-height: 27px;
    color: var(--white);
  }
</style>
</head>
<body>
<main class="ad">
  <svg class="ad__shapes" width="1200" height="899" viewBox="0 0 1200 899" aria-hidden="true">
    <defs>
      <linearGradient id="headerShade" x1="0" y1="0" x2="1" y2="0">
        <stop offset="0" stop-color="#3a3a3c"/>
        <stop offset="1" stop-color="#6e6e71"/>
      </linearGradient>
      <linearGradient id="nameBar" x1="0" y1="0" x2="1" y2="0">
        <stop offset="0" stop-color="#3a3a3c"/>
        <stop offset="1" stop-color="#6a6a6d"/>
      </linearGradient>
      <radialGradient id="sealFill" cx="0.4" cy="0.35" r="0.7">
        <stop offset="0" stop-color="#9a2a30"/>
        <stop offset="1" stop-color="#6a181d"/>
      </radialGradient>
      <linearGradient id="rankFill" x1="0" y1="0" x2="0" y2="1">
        <stop offset="0" stop-color="#e3c98f"/>
        <stop offset="1" stop-color="#a8874f"/>
      </linearGradient>
    </defs>
    <rect class="header" x="0" y="0" width="1200" height="315" fill="url(#headerShade)"/>
    <polygon class="header__facet" points="0,0 150,0 420,315 0,315" fill="#333335" opacity="0.55"/>
    <rect class="band" x="0" y="315" width="1200" height="185" fill="var(--gold)"/>
    <polygon class="practice-panel" points="0,500 580,500 810,778 0,778" fill="var(--mist)"/>
    <polygon class="name-bar" points="610,500 1200,500 1200,587 680,587" fill="url(#nameBar)"/>

    <g class="endorsements">
      <circle cx="852" cy="645" r="37" fill="#f4efe6" stroke="#c9a673" stroke-width="2"/>
      <circle cx="852" cy="645" r="31" fill="url(#sealFill)"/>
      <circle cx="852" cy="645" r="18" fill="none" stroke="#d9b76a" stroke-width="2"/>
      <rect x="941" y="617" width="80" height="57" fill="#d32323"/>
      <rect x="947" y="661" width="68" height="8" fill="#ffffff" opacity="0.35"/>
      <rect x="1072" y="617" width="80" height="57" rx="4" fill="url(#rankFill)"/>
      <rect x="890" y="712" width="107" height="41" rx="4" fill="#1d6a9c"/>
      <rect x="893" y="715" width="30" height="35" rx="2" fill="#ffffff"/>
      <circle cx="976" cy="736" r="11" fill="#ffffff"/>
      <polygon points="1040,750 1116,750 1110,764 1046,764" fill="#2a7fbf"/>
      <circle cx="1078" cy="731" r="33" fill="#ffffff" stroke="#2a86c9" stroke-width="4"/>
      <circle cx="1078" cy="731" r="24" fill="#e8f2fa"/>
    </g>

    <polygon class="address-tab" points="820,786 1200,786 1200,866 870,866" fill="var(--gold)"/>
    <polygon class="footer-strip" points="0,880 905,880 895,899 0,899" fill="var(--gold)"/>
  </svg>

  <div class="ad__portrait" role="img" aria-label="Portrait photograph of attorney Gordon R. Marvolin in a grey suit, white shirt and navy tie"></div>

  <div class="brand">MARVOLIN LAW<span class="brand__mark"></span></div>
  <div class="tagline">SHAPING FAITH WITH RESULTS</div>

  <p class="claim">KNOWN AND TRUSTED IN OUR<br>COMMUNITY FOR OVER 22 YEARS</p>

  <ul class="practices">
    <li class="practices__item"><svg width="16" height="16" viewBox="0 0 16 16"><polygon points="2,0 16,8 2,16 6,8" fill="#c9a673"/></svg>Personal Injury</li>
    <li class="practices__item"><svg width="16" height="16" viewBox="0 0 16 16"><polygon points="2,0 16,8 2,16 6,8" fill="#c9a673"/></svg>Legal Malpractice</li>
    <li class="practices__item"><svg width="16" height="16" viewBox="0 0 16 16"><polygon points="2,0 16,8 2,16 6,8" fill="#c9a673"/></svg>Unlicensed Contractors</li>
    <li class="practices__item"><svg width="16" height="16" viewBox="0 0 16 16"><polygon points="2,0 16,8 2,16 6,8" fill="#c9a673"/></svg>Medical Malpractice</li>
    <li class="practices__item"><svg width="16" height="16" viewBox="0 0 16 16"><polygon points="2,0 16,8 2,16 6,8" fill="#c9a673"/></svg>Civil Litigation</li>
  </ul>

  <div class="attorney">Gordon R. Marvolin, Esq.</div>

  <div class="contact contact--phone"><svg width="26" height="36" viewBox="0 0 26 36"><path d="M6 2 L11 2 L13 10 L9 13 Q11 22 16 26 L20 22 L25 27 L22 33 Q14 35 8 26 Q2 16 3 6 Z" fill="#c9a673"/></svg>(888) 555-0142</div>
  <div class="contact contact--web"><svg width="28" height="28" viewBox="0 0 28 28" fill="none" stroke="#c9a673" stroke-width="1.8"><circle cx="14" cy="14" r="12"/><ellipse cx="14" cy="14" rx="5.5" ry="12"/><line x1="2" y1="14" x2="26" y2="14"/><line x1="4" y1="8" x2="24" y2="8"/><line x1="4" y1="20" x2="24" y2="20"/></svg>marvolinlegal.com</div>

  <div class="address">2710 Larkmoor Ave. | Suite 408<br>Westbrook, CA | 90418</div>
</main>
</body>
</html>
```